New Flyer Design Project

I have an Upmarket Hair and Beauty Salon near the beach. I already have a current logo but it needs to change to Hair AND Beauty as we were only doing beauty. I want it to have a special on the flyer and to be DL size. I like it to be elegant with soft colours. I like the blues/teals also. I have attached the current business cards. I want it to tie in with the business cards somehow as well. I want the add to have something along the lines of - Mirabel & Tess now introduce to you Hair AND Beauty. We have combined our team to offer you all of your hair and beauty needs in the one great location! NEW CLIENTS OFFER $49 Style Cut & Blowdry and 30% off ALL Waxing

We are a Volaine and Cutivessa Salon so you can google to get the feel of the brand. The flyer will be used as a leaflet drop.
Please include an expiry of march 31st 2015
I would prefer not to use stock images also
Phone Number 08 9437 2854
shop 2&3 Corrow Point Blvd
Yanchep 6035

Thankyou :)

Target Market(s)

20-40

Industry/Entity Type

Hair

Requirements
Must have
• DL size
Address & Contact details
08 9437 2854
shop 7&8 Corrow Point Blvd
Marlow Bay 6071
Should not have
• Do not like clip arts-scissors etc
Would prefer not to use stock images

```html
<!DOCTYPE html>
<html lang="en">
<head>
<meta charset="utf-8">
<title>Mirabel &amp; Tess – New Clients Flyer</title>
<link href="https://fonts.googleapis.com/css2?family=Montserrat:wght@500;600;700&family=Roboto+Condensed:wght@700&family=Lora&display=swap" rel="stylesheet">
<style>
  :root {
    --page: #e9e7e4;
    --paper: #f4f4f5;
    --paper-shade: #dcdde0;
    --navy: #1f3f7a;
    --teal: #1a9a9a;
    --teal-line: #2aa7a3;
    --dark: #1c1a19;
    --dark-soft: #34302e;
    --gold: #f6e21c;
    --ink: #555a60;
    --white: #ffffff;
  }
  * { box-sizing: border-box; margin: 0; padding: 0; }
  html, body { width: 690px; height: 1200px; overflow: hidden; }
  body { background: var(--page); position: relative; font-family: "Montserrat", Arial, sans-serif; }

  .flyer {
    position: absolute; left: 85px; top: 60px; width: 520px; height: 1070px;
    background: radial-gradient(ellipse at 50% 40%, var(--white), var(--paper) 55%, var(--paper-shade));
    box-shadow: 0 3px 14px rgba(0,0,0,.18);
    overflow: hidden;
  }
  .flyer > * { position: absolute; left: 0; width: 100%; }

  .rule-teal { height: 7px; background: var(--teal-line); }
  .rule-navy { height: 5px; background: var(--navy); opacity: .75; }

  .header { top: 0; height: 160px; text-align: center; }
  .header .rule-teal, .header .rule-navy { position: absolute; left: 0; width: 100%; }
  .header .rule-teal { top: 0; }
  .header .rule-navy { top: 150px; }
  .brand {
    position: absolute; top: 44px; width: 100%;
    font-weight: 500; font-size: 52px; color: var(--navy); letter-spacing: -0.5px; line-height: 1;
  }
  .tagline {
    position: absolute; top: 106px; width: 100%;
    font-family: "Lora", Georgia, serif; font-size: 18px; color: var(--teal);
  }

  .band {
    background: linear-gradient(180deg, var(--dark-soft), var(--dark) 50%, var(--dark-soft));
    color: var(--white); text-align: center;
  }
  .band-offer { top: 165px; height: 232px; }
  .offer-box {
    position: absolute; left: 48px; top: 26px; width: 420px; height: 180px;
    border: 4px solid var(--white); padding-top: 24px;
  }
  .offer-title { font-weight: 600; font-size: 34px; letter-spacing: .5px; line-height: 1.1; }
  .offer-detail {
    font-family: "Roboto Condensed", Arial, sans-serif; font-weight: 700; font-size: 22px; margin-top: 4px;
  }
  .offer-detail .price { color: var(--gold); font-size: 24px; }
  .offer-waxing { font-weight: 600; font-size: 31px; margin-top: 2px; }

  .flourish {
    height: 64px;
    background: linear-gradient(90deg, rgba(31,63,122,.15), rgba(31,63,122,.45) 50%, rgba(31,63,122,.15));
  }
  .flourish-top { top: 397px; }

  .intro { top: 505px; text-align: center; }
  .intro .rule-navy { width: 420px; height: 3px; margin: 0 auto; }
  .intro-title {
    font-family: "Roboto Condensed", Arial, sans-serif; font-weight: 700;
    font-size: 52px; color: var(--teal); line-height: 1; margin: 8px 0 4px;
  }
  .intro-sub { font-weight: 600; font-size: 17.5px; color: var(--navy); margin-bottom: 8px; }
  .intro-body {
    width: 450px; margin: 24px auto 0; font-weight: 600; font-size: 16px; line-height: 1.5; color: var(--ink);
  }

  .rule-mid { top: 755px; }
  .band-contact { top: 765px; height: 140px; padding-top: 20px; }
  .address { font-weight: 600; font-size: 21px; line-height: 1.3; }
  .phone {
    display: inline-flex; align-items: center; gap: 10px; margin-top: 12px;
    font-weight: 700; font-size: 27px; color: var(--gold); letter-spacing: .5px;
  }
  .phone svg { width: 26px; height: 26px; }

  .rule-bottom { top: 918px; }
  .flourish-bottom { top: 960px; height: 90px; }
</style>
</head>
<body>
  <article class="flyer">
    <header class="header">
      <div class="rule-teal"></div>
      <div class="brand">Mirabel &amp; Tess</div>
      <div class="tagline">True hair &amp;beauty is timeless</div>
      <div class="rule-navy"></div>
    </header>

    <section class="band band-offer">
      <div class="offer-box">
        <div class="offer-title">NEW CLIENTS OFFER</div>
        <div class="offer-detail"><span class="price">$49</span> Style Cut &amp; Blowdry and <span class="price">30%</span> off</div>
        <div class="offer-waxing">ALL Waxing</div>
      </div>
    </section>

    <div class="flourish flourish-top" role="img" aria-label="Navy floral scroll ornament"></div>

    <section class="intro">
      <div class="rule-navy"></div>
      <h1 class="intro-title">MIRABEL &amp; TESS</h1>
      <p class="intro-sub">now introduce to you Hair AND Beauty</p>
      <div class="rule-navy"></div>
      <p class="intro-body">We have combined our team to offer you all of your hair and beauty needs in the one great location!We are a Volaine and Cutivessa Salon.</p>
    </section>

    <div class="rule-teal rule-mid"></div>

    <section class="band band-contact">
      <p class="address">shop 7&amp;8 Corrow Point Blvd<br>Marlow Bay 6071</p>
      <p class="phone">
        <svg viewBox="0 0 24 24" aria-hidden="true">
          <rect width="24" height="24" rx="5" fill="var(--gold)"/>
          <path d="M8.2 5.5c.4-.3 1-.2 1.3.2l1.5 2.3c.3.4.2 1-.2 1.3l-1 .8c.7 1.7 2.2 3.3 4 4.1l.8-1c.3-.4.9-.5 1.3-.2l2.3 1.5c.4.3.5.9.2 1.3l-1 1.4c-.5.6-1.3.9-2.1.6C11.2 16.5 7.5 12.8 6.2 8.9c-.3-.8 0-1.6.6-2.1z" fill="var(--dark)"/>
        </svg>
        08 9437 2854
      </p>
    </section>

    <div class="rule-teal rule-bottom"></div>
    <div class="flourish flourish-bottom" role="img" aria-label="Navy floral scroll ornament along the foot of the flyer"></div>
  </article>
</body>
</html>
```